Local electrical company needs two flyers designed

We are a small local electrical contracting company and are in desperate need of a awasome flyer design to help grow our business

hi everyone.

please keep the logo off the front page.
it can go on the rear.

We are really trying to portray a angry/frustrated women BECAUSE her lights are broken.
not light globes

Target Market(s)

Home owners

Industry/Entity Type

Electrical

Font styles to use
Serif

Requirements
Nice to have

```html
<!DOCTYPE html>
<html lang="en">
<head>
<meta charset="utf-8">
<title>Lighting Replacement Flyers</title>
<link rel="stylesheet" href="https://fonts.googleapis.com/css2?family=Arimo:wght@400;700&display=swap">
<style>
  :root {
    --page-bg: #ece6dd;
    --ink: #111111;
    --flyer-black: #050505;
    --flyer-navy: #0c1628;
    --photo-kitchen: #3a4258;
    --photo-kitchen-warm: #5b4f4c;
    --photo-spot: #2a4270;
    --photo-bill: #6f5a3c;
    --yellow: #f7e21b;
    --orange: #f7941d;
    --white: #ffffff;
  }
  * { margin: 0; padding: 0; box-sizing: border-box; }
  html, body { width: 865px; height: 1200px; overflow: hidden; }
  body {
    position: relative;
    background: var(--page-bg);
    font-family: "Arimo", Arial, sans-serif;
    color: var(--ink);
  }
  .sheet-label {
    position: absolute;
    left: 135px;
    font-size: 24px;
    font-weight: 400;
    line-height: 1;
    text-transform: uppercase;
  }
  .sheet-label--top { top: 97px; }
  .sheet-label--bottom { top: 1046px; left: 133px; }

  .flyer {
    position: absolute;
    left: 135px;
    width: 583px;
    height: 389px;
    overflow: hidden;
    color: var(--white);
    font-weight: 700;
    text-transform: uppercase;
  }
  .flyer--lighting { top: 141px; background: var(--flyer-black); }
  .flyer--downlight { top: 626px; background: var(--flyer-navy); }

  .photo-woman {
    position: absolute;
    inset: 0;
    background:
      linear-gradient(180deg, rgba(5,5,5,0) 0%, rgba(5,5,5,0) 55%, var(--flyer-black) 78%),
      linear-gradient(90deg, var(--flyer-black) 30%, var(--photo-kitchen) 62%, var(--photo-kitchen-warm) 80%, var(--photo-kitchen) 100%);
  }
  .photo-burning-bill {
    position: absolute;
    inset: 0;
    background:
      linear-gradient(180deg, rgba(12,22,40,0) 0%, rgba(12,22,40,0) 70%, var(--flyer-navy) 100%),
      linear-gradient(90deg, var(--flyer-navy) 35%, var(--photo-spot) 60%, var(--photo-bill) 85%, var(--photo-spot) 100%);
  }

  .headline {
    position: absolute;
    color: var(--yellow);
    font-size: 29px;
    line-height: 32px;
  }
  .flyer--lighting .headline { left: 35px; top: 26px; }
  .subline {
    position: absolute;
    font-size: 17px;
    line-height: 21px;
  }
  .flyer--lighting .subline--tired { left: 35px; top: 105px; }
  .flyer--lighting .subline--change { left: 35px; top: 185px; font-size: 20px; }

  .offer {
    position: absolute;
    left: 38px; top: 246px;
    display: flex; align-items: flex-end;
    line-height: 1;
  }
  .offer__amount { color: var(--orange); font-size: 95px; letter-spacing: -1px; }
  .offer__off { font-size: 32px; margin: 0 0 12px 8px; }
  .offer-tagline {
    position: absolute;
    left: 37px; top: 339px;
    font-size: 31.5px;
    line-height: 1;
  }
  .offer-tagline .accent { color: var(--yellow); }

  .flyer--downlight .headline { left: 36px; top: 40px; font-size: 36.5px; line-height: 42px; }
  .flyer--downlight .subline { left: 37px; top: 176px; font-size: 22px; line-height: 28px; letter-spacing: 0.6px; }
  .wallet-line {
    position: absolute;
    left: 36px; top: 286px;
    font-size: 41.5px;
    font-weight: 400;
    line-height: 47px;
  }
  .wallet-line .accent { color: var(--yellow); }
</style>
</head>
<body>
  <p class="sheet-label sheet-label--top">Front Page Lighting Replacement</p>

  <section class="flyer flyer--lighting">
    <div class="photo-woman" role="img" aria-label="Frustrated woman resting her head on her hand at a kitchen table in a dim kitchen"></div>
    <h1 class="headline">Is your lighting<br>frustrating you?</h1>
    <p class="subline subline--tired">Tired of coming<br>home to lights that<br>don’t always work?</p>
    <p class="subline subline--change">Thinking of a change?</p>
    <p class="offer"><span class="offer__amount">SAVE $25</span><span class="offer__off">OFF</span></p>
    <p class="offer-tagline">Your <span class="accent">lighting replacement</span></p>
  </section>

  <section class="flyer flyer--downlight">
    <div class="photo-burning-bill" role="img" aria-label="Two ceiling downlights shining above a burning hundred dollar bill"></div>
    <h1 class="headline">Tired of<br>replacing<br>bulbs?</h1>
    <p class="subline">Lights keep<br>flicking off?</p>
    <p class="wallet-line"><span class="accent">Burning</span> a<br>hole in your <span class="accent">wallet?</span></p>
  </section>

  <p class="sheet-label sheet-label--bottom">Front Page Downlight Replacement</p>
</body>
</html>
```